Magazine site

We are replacing this site www.thebrackmoorbuilder.com to almost be exactly like timberlandsweekly.com and theplankettfitter.com, except the engineer will display a blog article on the home page.
Updates

Industry/Entity Type

Engineer

Requirements
Must have
• Blog Article

```html
<!DOCTYPE html>
<html lang="en">
<head>
<meta charset="utf-8">
<title>The Brackmoor Builder</title>
<link rel="stylesheet" href="https://fonts.googleapis.com/css2?family=Arimo:wght@400;700&family=Open+Sans:wght@400;600&display=swap">
<style>
:root{
  --header:#23282c;
  --nav-top:#f7f9fa;
  --nav-bottom:#dde4e8;
  --nav-text:#22282c;
  --band:#a39a7c;
  --page:#d9d9d9;
  --panel:#ffffff;
  --text:#333333;
  --muted:#444444;
  --accent-blue:#1aa3d4;
  --link:#1b6a97;
  --red:#b8000c;
  --tab-grey:#666666;
  --box-grey:#efefef;
  --footer:#3a3f44;
  --footer-low:#d4d4d4;
}
*{box-sizing:border-box;margin:0;padding:0}
html,body{width:937px;height:1200px;overflow:hidden}
body{position:relative;background:var(--page);font-family:Arimo,Arial,sans-serif;color:var(--text)}
.abs{position:absolute}
.site-header{left:0;top:0;width:937px;height:110px;background:var(--header)}
.brand{left:95px;top:24px;color:#fff;font-family:"Open Sans",sans-serif;font-weight:400;line-height:1}
.brand .small{display:block;font-size:21px}
.brand .big{display:block;font-size:37px;margin-top:2px}
.search{left:650px;top:12px;width:202px;height:23px;display:flex}
.search .field{flex:1;background:#fff;border:1px solid #ccc;font-size:11px;color:#aaa;padding:5px 8px}
.search .btn{width:49px;background:var(--red);color:#fff;font-size:9px;display:flex;align-items:center;justify-content:center}
.nav{left:0;top:110px;width:937px;height:53px;background:linear-gradient(var(--nav-top),var(--nav-bottom));border-top:1px solid #c8d0d4;border-bottom:1px solid #b9c3c8}
.nav .tab{left:84px;top:-11px;width:62px;height:64px;background:linear-gradient(#d9e0e3,#e9eef0);border-radius:5px 5px 0 0}
.nav a{position:absolute;top:18px;font-size:15px;font-variant:small-caps;color:var(--nav-text);text-decoration:none;letter-spacing:.3px}
.band{left:0;top:163px;width:937px;height:355px;background:linear-gradient(var(--band),#b4ab8e)}
.slider{left:42px;top:176px;width:852px;height:295px;background:#fff;box-shadow:0 2px 6px rgba(0,0,0,.35)}
.slide{left:5px;top:5px;width:843px;height:285px;background:linear-gradient(100deg,#d9e2ea 0%,#c2cdd6 30%,#4b5058 55%,#e7dcc8 80%,#cfd6dc 100%)}
.arrow{top:135px}
.dots{left:418px;top:478px;display:flex;gap:3px}
.dots span{width:12px;height:12px;border-radius:50%;background:#4a4a4a;border:1px solid #333}
.dots .on{background:#d52b1e}
.panel{left:42px;top:497px;width:852px;height:571px;background:var(--panel);box-shadow:0 1px 6px rgba(0,0,0,.25)}
.about h1{left:61px;top:510px;font-size:25px;font-weight:700;color:var(--accent-blue)}
.copy{font-size:10.3px;line-height:15.5px;color:var(--text)}
.team-photo{left:58px;top:667px;width:202px;height:135px;background:linear-gradient(120deg,#c9b6a5,#6b6f78 50%,#e2e4e6);box-shadow:1px 2px 3px rgba(0,0,0,.35)}
.issue{left:56px;top:837px;width:541px;height:218px;background:var(--box-grey)}
.issue h2{position:absolute;left:14px;top:20px;font-size:12.5px;font-weight:400;color:#222}
.cover{left:10px;top:51px;width:122px;height:156px;background:linear-gradient(#3c8a9a,#6fb6a7 50%,#3f6a4a)}
.issue-title{left:151px;top:51px;font-family:"Open Sans",sans-serif;font-size:9.5px;color:var(--link);border-bottom:1px solid var(--link)}
.issue-copy{left:151px;top:79px;width:360px;font-family:"Open Sans",sans-serif;font-size:9.6px;line-height:15.5px;text-align:justify;color:#333}
.issue-link{left:195px;top:183px;font-family:"Open Sans",sans-serif;font-size:9.6px;color:var(--link)}
.issue-link u{text-decoration:none;border-bottom:1px solid var(--link)}
.news{left:618px;top:509px;width:266px;height:329px;border:1px solid #c4c4c4;background:#fff}
.news h3{position:absolute;left:10px;top:13px;font-size:12.5px;font-weight:400;color:#333}
.tabs{left:10px;top:38px;width:246px;height:30px;border-bottom:3px solid var(--red)}
.tabs span{position:absolute;top:0;width:79px;height:27px;color:#fff;font-size:12px;display:flex;align-items:center;justify-content:center}
.tabs .news-tab{left:0;background:var(--red)}
.tabs .blog-tab{left:80px;background:var(--tab-grey);border:1px solid #444}
.item{left:13px;width:240px;padding-bottom:9px;border-bottom:1px dotted #888}
.item b{display:block;font-size:10.5px;font-weight:400;color:var(--link);margin-bottom:3px}
.item p{font-size:9.8px;line-height:15.5px;color:var(--muted)}
.more{left:16px;top:304px;font-family:"Open Sans",sans-serif;font-size:10.5px;color:var(--link)}
.blog-label{left:618px;top:858px;font-family:"Open Sans",sans-serif;font-size:9.3px;color:var(--link);border-bottom:1px solid var(--link)}
.blog-photo{left:625px;top:886px;width:228px;height:102px;background:linear-gradient(160deg,#a8c1d6,#8c7a64 55%,#5c4a38);box-shadow:0 1px 3px rgba(0,0,0,.3)}
.blog-meta{left:618px;top:1000px;font-family:"Open Sans",sans-serif;font-size:9.6px;line-height:17px;color:#333}
.footer{left:0;top:1098px;width:937px;height:40px;background:var(--footer)}
.footer-links{left:44px;top:14px;font-size:9.8px;color:#fff;word-spacing:1px}
.social{top:13px;width:14px;height:14px;border-radius:2px}
.legal{left:0;top:1138px;width:937px;height:62px;background:linear-gradient(#e8e8e8,var(--footer-low))}
.legal p{position:absolute;left:45px;top:20px;font-family:"Open Sans",sans-serif;font-size:9.3px;line-height:15px;color:#222}
</style>
</head>
<body>
<header class="site-header abs">
  <div class="brand abs"><span class="small">The Brackmoor</span><span class="big">Builder</span></div>
  <div class="search abs"><div class="field">Type your text</div><div class="btn">SEARCH</div></div>
</header>

<nav class="nav abs">
  <div class="tab abs"></div>
  <a style="left:98px">Home</a>
  <a style="left:166px">Current issue</a>
  <a style="left:293px">Archives</a>
  <a style="left:390px">Advertise</a>
  <a style="left:487px">Subscribe</a>
  <a style="left:586px">About</a>
  <a style="left:660px">Contact</a>
</nav>

<div class="band abs"></div>
<section class="slider abs">
  <div class="slide abs" role="img" aria-label="Two engineers in yellow hard hats on a construction site with a crane behind"></div>
  <svg class="arrow abs" style="left:22px" width="22" height="34" viewBox="0 0 22 34"><path d="M18 2 L5 17 L18 32" fill="none" stroke="#3a3a3a" stroke-width="6"/></svg>
  <svg class="arrow abs" style="left:808px" width="22" height="34" viewBox="0 0 22 34"><path d="M4 2 L17 17 L4 32" fill="none" stroke="#3a3a3a" stroke-width="6"/></svg>
</section>
<div class="dots abs"><span></span><span class="on"></span><span></span><span></span><span></span><span></span></div>

<main class="panel abs"></main>
<section class="about">
  <h1 class="abs">About us</h1>
  <p class="copy abs" style="left:61px;top:544px;width:530px">Lorem ipsum dolor sit amet, consectetur adipisicing elit, sed do eiusmod tempor incididunt ut labore et dolore magna aliqua. Ut enim ad minim veniam, quis nostrud exercitation ullamco laboris nisi ut aliquip ex ea commodo consequat.</p>
  <p class="copy abs" style="left:61px;top:590px;width:530px;height:62px;overflow:hidden">Lorem ipsum dolor sit amet, consectetur adipisicing elit, sed do eiusmod temporLorem ipsum dolor sit amet, consectetur adipisicing elit, sed do eiusmod tempor incididunt ut labore et dolore magna aliqua. Ut enim ad minim veniam, quis nostrud exercitation ullamco laboris nisi ut aliquip ex ea commodo consequat.Lorem ipsum dolor sit amet, consectetur adipisicing elit, sed do eiusmod temporLorem ipsum dolor sit amet, consectetur adipisicing elit, sed do eiusmod tempor incididunt ut labore et dolore</p>
  <div class="team-photo abs" role="img" aria-label="Smiling team of business people"></div>
  <p class="copy abs" style="left:283px;top:667px;width:313px;text-align:justify">Lorem Ipsum is simply dummy text of the printing and typesetting industry. Lorem Ipsum has been the industry's standard dummy text ever since the 1500s, when an unknown printer took a galley of type and scrambled it to make a type specimen book<br>Lorem Ipsum has been theindustry's standard dummy text ever since the 1500s,<br>&nbsp;when an unknown printer took a galley of type and scrambled it to make a type specimen book</p>
</section>

<section class="issue abs">
  <h2>LATEST ISSUE</h2>
  <div class="cover abs" role="img" aria-label="Magazine cover with aerial view of a solar field"></div>
  <div class="issue-title abs">BRACKMOOR BUILDER FEB/MARCH 2012</div>
  <p class="issue-copy abs">The 48-acre Ashcombe Hollow Landfill has been transformed into the largest solar energy generating facility in the region. The solar enegery cover produces more than 1 megawatt of renewable electricity - enough to power 224 homes. The Ashcombe Hollow Landfill closure represents a milestone in the solid waste industry because it provides many environmental and economical advantages. The system creates clean, renewable solar energy.</p>
  <svg class="abs" style="left:153px;top:176px" width="28" height="28" viewBox="0 0 28 28"><circle cx="14" cy="14" r="13" fill="#fff" stroke="#1b4f9a" stroke-width="2"/><circle cx="14" cy="14" r="8" fill="#f2b31b"/></svg>
  <div class="issue-link abs">View the latest magazine issue <u>click here</u></div>
</section>

<aside class="news abs">
  <h3>NEWS &amp; BLOG</h3>
  <div class="tabs abs"><span class="news-tab">NEWS</span><span class="blog-tab">Blog</span></div>
  <div class="item abs" style="top:86px"><b>lorem ipsum dolar sit amet</b><p>lorem ipsum dolar site amet lorem ipsum dlola sit amet lorem 31 may 2012 to 03 august 2012</p></div>
  <div class="item abs" style="top:155px"><b>lorem ipsum dolar sit amet</b><p>lorem ipsum dolar site amet lorem ipsum dlola sit amet lorem 31 may 2012 to 03 august 2012</p></div>
  <div class="item abs" style="top:231px"><b>lorem ipsum dolar sit amet</b><p>lorem ipsum dolar site amet lorem ipsum dlola sit amet lorem 31 may 2012 to 03 august 2012</p></div>
  <div class="more abs">View More ::</div>
</aside>

<div class="blog-label abs">LATEST BLOG POST</div>
<div class="blog-photo abs" role="img" aria-label="Construction workers tying rebar on a site"></div>
<div class="blog-meta abs">October 6, 2009<br>Business of Engineering and Education</div>

<footer class="footer abs">
  <div class="footer-links abs">HOME &nbsp;| &nbsp;CURRENT ISSUE &nbsp;| &nbsp;ARCHIVES &nbsp;| &nbsp;ABOUT US</div>
  <span class="social abs" style="left:837px;background:#1d7bb8"></span>
  <span class="social abs" style="left:856px;background:#3b5fa0"></span>
  <span class="social abs" style="left:875px;background:#8a8a8a"></span>
</footer>
<div class="legal abs"><p>Copyright Information<br>©2008 TheBrackmoorBuilder.Com [TM], All Rights Reserved.</p></div>
</body>
</html>
```